120ml Jar Label — Masculine Cosmetic Foot Balm for Cracked, Hardworking Heels

We need a print-ready wraparound label for a 120ml jar — a brown/amber glass jar with a black metal screw lid (file photo attached).

--DO NOT PUT A BARCODE ON THE LABEL PLEASE--
**PLEASE READ "PIXEL HARBOUR PROJECT BRIEF FINAL.MD" IN ATTACHED FILES IF YOU ARE SUBMITTING A DESIGN.**

The label is 190mm wide × 40mm high.
We need files to be in an .ai format with a 2mm bleed at the end.
Social media handle: @tallowgatenz (facebook, instagram and tiktok)

Tallow Gate is a New Zealand foot-care brand making practical, no-nonsense products for hardworking men whose jobs wreck their feet. Our flagship product, Ridge Mender Balm, helps fix thick, cracked, hardworking skin.

Brand color scheme and overview is all in the brief file. You may add some brand aligned colors outside of the specified hex codes as you see fit to make a great design. Feel free to remove the "Tallow Gate" text from the logo so Tallow Gate is not doubled up on the front of the label

The tone we want: direct, rugged, and credible — like a workwear brand, not a spa brand. Most cracked-heel products on the market lean soft and feminine; we want to stand apart by looking like a serious fix for a real problem, made in New Zealand.

Full legal requirements for New Zealand cosmetic labelling (ingredients, directions, net contents, origin, etc.) are listed in the attached brief document — these are non-negotiable and must stay legible.

Please see the label attached "Label spacing guide" for this project's rough spacing guide. This label is the same size and sits well on the jar. This label doesn't need to be spaced quite as much as the Brisko Label

I want to run the design for a week - I feel 7 days is a good amount of time for designers to see the work, digest the brief and create something remarkable and memorable for Tallow Gate.

Target Market(s)

Working men in New Zealand whose jobs or lifestyle put heavy wear on their feet — tradies, farmers, hospital/shift workers, hunters, and outdoors people. Practical, value-driven buyers rather than luxury skincare shoppers.

Industry/Entity Type

Beauty / Health & Wellness / Cosmetics

Font styles to use
Sans Serif
Other font styles liked:
• Montserrat (bold, headings), Inter (regular, body)

Colors
00AB8E
00BBA5
67D7C9
C6EFE9
E9F9F6
FFC000
F8CF3A
FAE287
FDF2CF
FEFAEE

Requirements
Must have
• All NZ cosmetic labelling requirements from the attached brief (product name, tag line, net contents, ingredients, directions, storage, made in NZ) — legible and complete, not omitted for aesthetics Fits 190mm × 40mm wraparound format for a 120ml brown jar with black lid Uses our existing brand colors: Deep Olive #3C4A34, Bone White #F4EFE6, Terracotta Clay #C1683D, and Warm Grey #4A4540 (exact palette in attached brief) Uses Montserrat (headings) and Inter (body) or close equivalents Incorporates our existing shield-and-wing logo (attached) Brand name and product name clearly readable from a normal shelf/bathroom-cabinet distance
Nice to have
• A style that could extend into a hero/product photo later, similar to the NZ-hills-backdrop look on our website (screenshot attached) — not required for the label itself, just good to keep in mind Original icon work (e.g. a small soak/apply/sock icon set) if it fits the rugged brand feel A design that could work as a small back-label/wraparound split if the front can't fit everything at a readable size
Should not have
• No pastel colors, floral motifs, or delicate script fonts — this should never look like spa/luxury skincare. Don't introduce new brand colors outside the palette provided other than black.

```html
<!DOCTYPE html>
<html lang="en">
<head>
<meta charset="utf-8">
<title>Tallow Gate – Ridge Mender Balm jar label</title>
<link href="https://fonts.googleapis.com/css2?family=Montserrat:wght@700;800&family=Inter:wght@400;500;700&family=Jost:wght@400;600&display=swap" rel="stylesheet">
<style>
  :root {
    --olive: #3c4a34;
    --bone: #f4efe6;
    --clay: #c1683d;
    --warm-grey: #4a4540;
    --ink: #1f2a1c;
    --page: #d6d5d8;
  }
  * { box-sizing: border-box; margin: 0; padding: 0; }
  html, body { width: 1200px; height: 940px; overflow: hidden; background: var(--page); }
  body { position: relative; font-family: "Inter", sans-serif; }

  .label {
    position: absolute; left: 30px; top: 338px;
    width: 1140px; height: 264px;
    background: var(--bone); overflow: hidden;
  }
  .band-top { position: absolute; left: 0; top: 0; width: 100%; height: 114px; background: var(--olive); }
  .band-mid { position: absolute; left: 0; top: 114px; width: 100%; height: 34px; background: var(--clay); }

  /* left panel */
  .panel-text {
    position: absolute; left: 22px; width: 331px;
    font-size: 12.6px; line-height: 19px; text-align: justify;
  }
  .ingredients { top: 14px; color: var(--bone); }
  .directions { top: 159px; color: var(--ink); }
  .tag {
    margin-left: -22px; padding: 1px 8px 1px 22px;
    font-weight: 700; color: var(--bone);
  }
  .ingredients .tag { background: var(--clay); }
  .directions .tag { background: var(--olive); }
  .storage {
    position: absolute; left: 22px; top: 116px; width: 331px;
    font-size: 12.6px; line-height: 15px; color: var(--bone);
  }
  .storage b { font-weight: 700; }

  /* front panel */
  .brand-mark {
    position: absolute; left: 470px; top: 22px; width: 200px;
    display: flex; flex-direction: column; align-items: center; gap: 8px;
  }
  .brand-mark .dot { width: 46px; height: 46px; border-radius: 50%; background: var(--bone); }
  .brand-mark .name { font-family: "Montserrat", sans-serif; font-weight: 700; font-size: 17px; color: var(--bone); }
  .brand-line {
    position: absolute; left: 380px; top: 117px; width: 300px; text-align: center;
    font-size: 26px; color: var(--bone); line-height: 28px;
  }
  .brand-line small { font-size: 16px; color: var(--olive); }
  .product-name {
    position: absolute; left: 410px; top: 154px; max-width: 262px;
    font-family: "Montserrat", sans-serif; font-weight: 800; white-space: nowrap;
    font-size: 31px; line-height: 36px; color: var(--olive);
  }
  .rule { position: absolute; left: 380px; top: 229px; width: 226px; height: 1px; background: var(--ink); }
  .tagline { position: absolute; left: 414px; top: 232px; font-size: 18px; color: var(--clay); }
  .origin-stamp {
    position: absolute; left: 680px; top: 170px; width: 60px; height: 60px;
    border-radius: 50%; border: 2px solid var(--clay);
  }
  .net-contents {
    position: absolute; left: 690px; top: 236px;
    font-family: "Jost", sans-serif; font-weight: 600; font-size: 17px; color: var(--ink);
  }
  .net-contents small { font-size: 11px; }

  /* right panel */
  .badges { position: absolute; left: 806px; top: 25px; display: flex; gap: 10px; }
  .badge { width: 64px; height: 64px; border-radius: 50%; border: 1.5px solid var(--bone); }
  .web-row {
    position: absolute; left: 793px; top: 114px; height: 34px;
    display: flex; align-items: center; gap: 12px; color: var(--bone);
  }
  .web-row .url { font-size: 18px; letter-spacing: 1.2px; }
  .web-row .handle { font-size: 12px; font-weight: 500; }
  .contacts {
    position: absolute; left: 849px; top: 157px; width: 200px; text-align: center;
    font-family: "Jost", sans-serif; font-size: 12px; line-height: 15px; color: var(--ink);
  }
  .contacts h3 { font-size: 12px; font-weight: 600; }
  .contacts p + h3 { margin-top: 10px; }
</style>
</head>
<body>
  <section class="label">
    <div class="band-top"></div>
    <div class="band-mid"></div>

    <p class="panel-text ingredients"><span class="tag">Ingredients :</span> Shea Butter, Beef Tallow, Beeswax, Grape Seed Oil, Vegetable Glycerin, Lanolin, Panthenol, Gluconolactone &amp; Sodium Benzoate, Manuka Honey, Allantoin, Vitamin E, Tea Tree Essential Oil, Lemon Myrtle Essential Oil, Rosemary Oleoresin Extract</p>
    <p class="storage"><b>Storage:</b> Keep out of direct sunlight. Best used within six months of opening.</p>
    <p class="panel-text directions"><span class="tag">Directions :</span> Apply generously to clean, dry feet, focusing on heels and thick or cracked areas. For cracked heels, wear our moisture-locking socks overnight. Use daily.</p>

    <div class="brand-mark">
      <span class="dot"></span>
      <span class="name">Tallow Gate</span>
    </div>
    <p class="brand-line">Tallow Gate<small>NZ</small></p>
    <h1 class="product-name">Ridge Mender<br>Balm</h1>
    <div class="rule"></div>
    <p class="tagline">For Hardworking Soles</p>
    <div class="origin-stamp" role="img" aria-label="Made in New Zealand stamp"></div>
    <p class="net-contents">120<small>ml</small></p>

    <div class="badges">
      <span class="badge" role="img" aria-label="Handmade badge"></span>
      <span class="badge" role="img" aria-label="100% natural ingredients badge"></span>
      <span class="badge" role="img" aria-label="For all skin types badge"></span>
      <span class="badge" role="img" aria-label="Hydrating badge"></span>
    </div>
    <div class="web-row">
      <span class="url">www.tallowgate.co.nz</span>
      <span class="handle">@tallowgatenz</span>
    </div>
    <div class="contacts">
      <h3>MANUFACTURER:</h3>
      <p>18 Kauri Lane, 3110<br>Tauranga New Zealand.</p>
      <h3>DISTRIBUTOR:</h3>
      <p>52 Harbour Road, Petone,<br>Lower Hutt 5012, New Zealand.</p>
    </div>
  </section>
</body>
</html>
```